Metal Fabrication Business Cards

We need a business card for our business of Metal Fabrication/Welding. Our company is called "Hadley's Metal Fabrication"

We are a metal fabrication business which takes on "high class" clients- dealing with some of the biggest builders in Australia. Our work is neat, and the type of work we do is 2nd to none for quality. We want to show that on our cards. However, we would love to show a side that is down to earth and a bit more modern and contemporary - we are all young in business so would love to show that side - rather than a boring "very straight looking" card. We always have a clean workshop and take pride in our presentation. We want to come across like we are very rich, but would love to go for a surf as well! A card that basically says we have high class and will charge you a high rate - but the quality will be outstanding.

Front of card: - Simply but sharp!
-Thinking maybe white card - with nice black writing.
-On the right hand side of card a person welding - or holding a welder.
- My business name - Hadley's Metal Fabrication
-Also maybe my name - which is 'Corey" (if it doesn't work, we can put this on the back of card.)
- if needed to look better - we can put keywords on front of card like "metal fabrication, sheet metal, welding etc" but I dont want it to be crowded.

Back of card: - Also make smart but sharp!
Put details such as:
04387 21 914
hadley.fabrication@tinmailbox.com.au
7/32 Keel Street
North Tarrant NSW 2471
www.korvinfabrication.com.au
ABN 72 615 803 914

thats just an idea - its now up to you. I don't mind what you come up with - as long as it stands out from the rest and looks sharp, professional but contemporary.

Business

Put details such as:
04387 21 914
7/32 Keel Street
North Tarrant NSW 2471
ABN 72 615 803 914

Hadley's Metal Fabrication

```html
<!DOCTYPE html>
<html lang="en">
<head>
<meta charset="utf-8">
<title>Hadley's Metal Fabrication – Business Cards</title>
<link rel="stylesheet" href="https://fonts.googleapis.com/css2?family=Barlow:wght@400;500;600;700&display=swap">
<style>
  :root {
    --page: #e8e6e3;
    --card: #0d0d0e;
    --ink: #f2f2f2;
    --steel: #c9cacc;
    --steel-dark: #6f7175;
    --photo-deep: #1a1440;
    --photo-mid: #3a2f9a;
    --photo-glow: #7e6cf0;
    --spark: #e9a0c0;
  }
  * { box-sizing: border-box; margin: 0; padding: 0; }
  html, body { width: 1200px; height: 1200px; overflow: hidden; }
  body {
    background: var(--page);
    font-family: "Barlow", "Helvetica Neue", Arial, sans-serif;
    color: var(--ink);
    position: relative;
  }
  .card {
    position: absolute;
    left: 230px;
    width: 740px;
    height: 450px;
    background: var(--card);
    overflow: hidden;
    box-shadow: 0 10px 24px rgba(0,0,0,0.25);
  }
  .card--front { top: 110px; }
  .card--back { top: 640px; }

  /* Front */
  .welder-photo {
    position: absolute;
    left: 0; top: 0;
    width: 470px; height: 100%;
    background:
      radial-gradient(circle at 14% 68%, var(--spark) 0%, var(--photo-glow) 10%, transparent 32%),
      radial-gradient(ellipse at 45% 35%, var(--photo-mid) 0%, transparent 60%),
      linear-gradient(100deg, var(--photo-deep) 0%, #241c66 55%, var(--card) 100%);
  }
  .brand {
    position: absolute;
    text-transform: uppercase;
    font-weight: 700;
    color: var(--steel);
    line-height: 1;
  }
  .card--front .brand { right: 40px; top: 68px; text-align: right; }
  .brand__name { display: block; font-size: 52px; letter-spacing: 3px; }
  .brand__trade { display: block; font-size: 21px; letter-spacing: 5px; margin-top: 10px; }

  .services {
    position: absolute;
    right: 70px; top: 190px;
    list-style: none;
    text-align: right;
    font-size: 22px;
    font-weight: 500;
    letter-spacing: 2.5px;
    text-transform: uppercase;
    line-height: 33px;
  }

  /* Back */
  .card--back .brand { left: 36px; top: 42px; }
  .card--back .brand__name { font-size: 40px; letter-spacing: 2px; }
  .card--back .brand__trade { font-size: 16px; letter-spacing: 4px; margin-top: 8px; }

  .holder {
    position: absolute;
    left: 120px; top: 222px;
    font-size: 34px;
    font-weight: 700;
    letter-spacing: 2px;
    text-transform: uppercase;
  }
  .holder-rule {
    position: absolute;
    left: 0; top: 270px;
    width: 245px; height: 4px;
    background: linear-gradient(90deg, var(--steel-dark), var(--steel));
  }
  .contact {
    position: absolute;
    left: 320px; top: 132px;
    width: 390px;
    list-style: none;
    font-size: 18px;
    letter-spacing: 1px;
  }
  .contact__item { display: flex; align-items: flex-start; gap: 12px; margin-bottom: 16px; line-height: 22px; white-space: nowrap; }
  .contact__icon { width: 20px; height: 22px; flex: none; fill: var(--ink); }
  .contact__abn { padding-left: 32px; }
</style>
</head>
<body>

<section class="card card--front" aria-label="Card front">
  <div class="welder-photo" role="img" aria-label="Photo of a welder in a mask working with bright sparks under blue light"></div>
  <div class="brand">
    <span class="brand__name">Hadley's</span>
    <span class="brand__trade">Metal Fabrication</span>
  </div>
  <ul class="services">
    <li>Sheet Metal</li>
    <li>Welding</li>
    <li>Stainless</li>
    <li>Aluminium</li>
    <li>Frames</li>
    <li>Brackets</li>
    <li>Custom Made</li>
  </ul>
</section>

<section class="card card--back" aria-label="Card back">
  <div class="brand">
    <span class="brand__name">Hadley's</span>
    <span class="brand__trade">Metal Fabrication</span>
  </div>
  <p class="holder">Corey</p>
  <div class="holder-rule"></div>
  <ul class="contact">
    <li class="contact__item">
      <svg class="contact__icon" viewBox="0 0 20 22" aria-hidden="true"><rect x="4" y="1" width="12" height="20" rx="2" fill="none" stroke="#f2f2f2" stroke-width="2"/><rect x="7" y="4" width="6" height="6" /><circle cx="10" cy="17" r="1.3"/></svg>
      <span>04387 21 914</span>
    </li>
    <li class="contact__item">
      <svg class="contact__icon" viewBox="0 0 20 22" aria-hidden="true"><rect x="2" y="6" width="16" height="11"/><path d="M2 6 L10 12 L18 6" fill="none" stroke="#0d0d0e" stroke-width="1.6"/></svg>
      <span>hadley.fabrication@tinmailbox.com.au</span>
    </li>
    <li class="contact__item">
      <svg class="contact__icon" viewBox="0 0 20 22" aria-hidden="true"><path d="M10 1a7 7 0 0 0-7 7c0 5 7 13 7 13s7-8 7-13a7 7 0 0 0-7-7z"/><circle cx="10" cy="8" r="2.6" fill="#0d0d0e"/></svg>
      <span>7/32 Keel Street<br>North Tarrant NSW 2471</span>
    </li>
    <li class="contact__item">
      <svg class="contact__icon" viewBox="0 0 20 22" aria-hidden="true"><circle cx="10" cy="11" r="8.5"/><path d="M5 7 q3 1 4 4 q-2 3 -1 6 M12 4 q1 3 4 4 q-2 2 -1 5" fill="none" stroke="#0d0d0e" stroke-width="1.6"/></svg>
      <span>www.korvinfabrication.com.au</span>
    </li>
    <li class="contact__item contact__abn">ABN 72 615 803 914</li>
  </ul>
</section>

</body>
</html>
```